Buisness cards for international property developer
Morelli Costruzioni Group
Professional
Beatrice Solange Morelli
CEO
Head Office: Via Campo Lungo 158 00149 Rome Italy
beatrice.morelli@morellicostruzionigroup.com
www.morellicostruzionigroup.com

```html
<!DOCTYPE html>
<html lang="en">
<head>
<meta charset="utf-8">
<title>Morelli Costruzioni Group – Business Cards</title>
<link rel="stylesheet" href="https://fonts.googleapis.com/css2?family=Cinzel:wght@400;600&family=Libre+Baskerville:wght@400;700&display=swap">
<style>
  :root {
    --bg: #e9e6e1;
    --card: #ffffff;
    --gold: #c48a24;
    --ink: #2f2f2f;
    --muted: #6b6b6b;
    --shadow: rgba(0,0,0,0.18);
  }
  * { margin: 0; padding: 0; box-sizing: border-box; }
  html, body { width: 1200px; height: 980px; overflow: hidden; background: var(--bg); }
  .canvas { position: relative; width: 1200px; height: 980px; }
  .card {
    position: absolute; left: 220px; width: 760px; height: 434px;
    background: var(--card); box-shadow: 0 6px 22px var(--shadow); overflow: hidden;
  }
  .card--front { top: 40px; }
  .card--back { top: 506px; }

  /* Front */
  .brand { position: absolute; display: flex; align-items: center; gap: 14px; }
  .brand__mark { width: 30px; height: 30px; background: var(--gold); }
  .brand__name {
    font-family: "Cinzel", serif; font-weight: 400; color: var(--gold);
    letter-spacing: 0.04em; text-transform: uppercase; white-space: nowrap;
  }
  .card--front .brand { left: 56px; top: 66px; }
  .card--front .brand__name { font-size: 17px; }

  .holder { position: absolute; left: 56px; top: 180px; }
  .holder__name {
    font-family: "Libre Baskerville", serif; font-weight: 700; font-size: 27px;
    color: var(--gold); border-bottom: 2px solid var(--gold); padding-bottom: 4px;
  }
  .holder__role {
    font-family: "Libre Baskerville", serif; font-weight: 700; font-size: 16px;
    color: var(--ink); margin-top: 8px;
  }

  .office {
    position: absolute; left: 470px; top: 60px;
    font-family: "Libre Baskerville", serif; font-weight: 700; font-style: normal;
    font-size: 16px; line-height: 1.55; color: var(--ink);
  }

  .corner-pattern { position: absolute; right: 0; top: 0; width: 220px; height: 220px; }

  .contact {
    position: absolute; left: 56px; right: 56px; bottom: 36px;
    display: flex; gap: 28px;
    font-family: "Libre Baskerville", serif; font-size: 13px; color: var(--gold);
  }

  /* Back */
  .card--back .brand { left: 56px; top: 196px; flex-direction: column; align-items: flex-start; gap: 8px; }
  .card--back .brand__name {
    font-size: 17px; color: var(--muted);
    border-bottom: 1px solid var(--muted); padding-bottom: 4px;
  }
  .brand__tagline {
    font-family: "Cinzel", serif; font-size: 9px; letter-spacing: 0.25em;
    color: var(--muted); align-self: flex-end; white-space: nowrap;
  }
  .diamond-pattern { position: absolute; left: 425px; top: 67px; width: 300px; height: 300px; }
</style>
</head>
<body>
<main class="canvas">
  <section class="card card--front">
    <div class="brand">
      <span class="brand__mark"></span>
      <span class="brand__name">Morelli Costruzioni Group</span>
    </div>

    <div class="holder">
      <h1 class="holder__name">Beatrice Solange Morelli</h1>
      <p class="holder__role">CEO</p>
    </div>

    <address class="office">
      Head Office:<br>
      Via Campo Lungo 158<br>
      00149 Rome<br>
      Italy
    </address>

    <svg class="corner-pattern" viewBox="0 0 220 220" role="img" aria-label="Gold geometric brand pattern in the card corner">
      <polygon points="40,0 220,0 220,180" fill="var(--gold)"/>
    </svg>

    <p class="contact">
      <span>beatrice.morelli@morellicostruzionigroup.com</span>
      <span>www.morellicostruzionigroup.com</span>
    </p>
  </section>

  <section class="card card--back">
    <div class="brand">
      <span class="brand__name">Morelli Costruzioni Group</span>
      <span class="brand__tagline">Develop · Build · Invest</span>
    </div>

    <svg class="diamond-pattern" viewBox="0 0 300 300" role="img" aria-label="Large gold diamond filled with a repeating brand pattern">
      <polygon points="150,0 300,150 150,300 0,150" fill="var(--gold)"/>
    </svg>
  </section>
</main>
</body>
</html>
```